Regional and National Rugby Training and Player Development Company

We need a new responsive website design that is easy to navigate and encourages people to register for our programs.

Registration and payment could be written into the site but it can also be externally integrated as it is currently.

I want clean lines, bright images, and a webpage that is easy to update and manage. Currently using WordPress.
Updates

Keelstone Rugby runs four programs:  Youth Summer Rugby Camps, Winter Indoor Touch Rugby, Spring Training Camps, and the "Player Development Program" otherwise known as the Academy

Ultimately, Keelstone Rugby wants to attract the top players across the province of Ontario to join our corner-stone program, the Winter Academy.

We have had many players play at the provincial level and a select handful go on to represent Canada.  We aspire to set the standard for off-season junior rugby player development.

Reason: 1) Laptop crashed on Thurs. which meant I couldn't make a fair decision this weekend. 2). There are FIVE very good designs, each somewhat unique. I want to see what designers come up with when I outline what I like in each as a requirement of what has been provided. Thank you for your understanding and efforts in this regard. Sincerely, MB Sent from my iPad

Thank you for all your efforts and patience in this design campaign, I truly appreciate it.  Apologies for the lack of communication but as a full-time high school teacher, sometimes my "real job" gets put to the side.  

I have reduced over 30 designs to five... you are the five remaining I hope to take certain aspects of each that I like best and provide some feedback to you the designers, in order to make final adjustments before my final decision.

I hope you find this process agreeable and again, thank you for your patience and efforts in this campaign.  I think each of your designs look fantastic and are a drastic and valuable improvement of what I have been using up to this point.

Appreciatively,

MB

Voting poll results are in and there are three distinct leaders... going to focus on these three this week and come to a final decision before Friday.

Each designer will be contacted privately to provide some feedback and see what the best final product can look like.

Thank you for your patience and high-quality work!

MB

Reason: Just too much going on at the moment and trying to stay on top of this. Apologies to all. Just had the results of the voting poll come in and have reduced choices to two clear leaders with a third alternate. Going to provide feedback for all three today and hope to make final decision by Friday. Thank you for your efforts.

Target Market(s)

Junior rugby players (boys and girls) between the ages of 12 and 20... more importantly, their parents!

Industry/Entity Type

It Company

Requirements
Must have
• Must have high-resolution, clean lines, and encourage registration in programs. I would like it to be integrated with my YouTube page as well as other social media.

```html
<!DOCTYPE html>
<html lang="en">
<head>
<meta charset="utf-8">
<title>Keelstone Rugby Canada</title>
<link rel="stylesheet" href="https://fonts.googleapis.com/css2?family=Oswald:wght@300;400;500&family=Pathway+Gothic+One&display=swap">
<style>
:root{
  --red:#d2232a;
  --red-dark:#b30a0a;
  --ink:#3a3a3a;
  --muted:#5e5e5e;
  --rule:#dedede;
  --panel:#f0f0f0;
  --band:#4a4a4a;
  --black:#0c0c0c;
  --white:#ffffff;
}
*{margin:0;padding:0;box-sizing:border-box}
html,body{width:900px;height:1200px;overflow:hidden;background:var(--white)}
body{position:relative;font-family:"Pathway Gothic One",sans-serif;color:var(--muted)}
.abs{position:absolute}
.heading{font-family:"Oswald",sans-serif;font-weight:400;text-transform:uppercase;color:var(--ink);font-size:19px;line-height:1}
.heading em{font-style:normal;color:var(--red)}
.body-text{font-size:11.5px;line-height:17.4px;color:var(--muted)}

/* header */
.site-header{left:0;top:0;width:900px;height:94px;background:linear-gradient(90deg,#1a1a1a 0%,#2e2e2e 30%,#111 60%,#000 100%)}
.brand{left:98px;top:20px;display:flex;align-items:center;gap:10px}
.brand-mark{width:40px;height:40px;border-radius:50%;background:var(--red)}
.brand-name{font-family:"Oswald",sans-serif;font-weight:500;color:var(--red);font-size:17px;line-height:20px;letter-spacing:1px;text-transform:uppercase}
.social{left:730px;top:13px;display:flex;gap:7px}
.social span{width:16px;height:16px;background:#8a8a8a;border-radius:2px}
.search{left:707px;top:37px;width:131px;height:19px;background:#3a3a3a;border-radius:2px}
.search svg{position:absolute;right:5px;top:3px}
.main-nav{left:0;top:64px;width:900px;height:30px}
.main-nav a{position:absolute;top:0;font-family:"Oswald",sans-serif;font-weight:400;font-size:14.5px;color:var(--white);text-decoration:none;letter-spacing:.3px}
.main-nav a.active::after{content:"";position:absolute;left:-8px;right:-8px;top:26px;height:3px;background:var(--red)}

/* hero */
.hero{left:0;top:94px;width:900px;height:305px;background:radial-gradient(ellipse at 30% 45%,#3a3020 0%,#1c1a18 30%,transparent 55%),radial-gradient(ellipse at 65% 60%,#b8343a 0%,transparent 40%),linear-gradient(90deg,#6b4d56 0%,#8a5560 35%,#a0404a 60%,#5a3b44 85%,#7a5a66 100%)}
.hero-caption{left:0;top:218px;width:900px;text-align:center;font-family:"Oswald",sans-serif;font-weight:300;font-size:24px;color:var(--white)}
.hero-dots{left:417px;top:279px;display:flex;gap:6px}
.hero-dots span{width:12px;height:12px;border-radius:50%;background:#cfcfcf}
.hero-dots span:first-child{background:var(--white)}

/* rules */
.rule{height:3px;background:var(--rule)}
.hair{height:1px;background:var(--rule)}

/* programs */
.video{left:97px;top:725px;width:250px;height:152px;border:2px solid #c9c9c9;background:linear-gradient(180deg,#4a5560 0%,#7d8890 40%,#4f6b3a 60%,#3f5a2e 100%)}
.video .play{position:absolute;left:107px;top:60px}
.video .bar{position:absolute;left:0;right:0;bottom:0;height:10px;background:#1a1a1a}
.video .bar i{position:absolute;left:0;top:0;width:68px;height:2px;background:var(--red)}
.program-title{left:370px;top:722px;font-family:"Oswald",sans-serif;font-weight:300;font-size:15px;color:var(--red)}
.program-lead{left:370px;top:744px;font-size:12px;color:var(--muted)}
.checklist{left:371px;top:766px;list-style:none}
.checklist li{display:flex;align-items:center;gap:7px;height:24.6px;font-size:12px;color:var(--muted)}
.btn-register{left:367px;top:850px;width:106px;height:27px;background:var(--red);color:var(--white);border-radius:3px;font-family:"Oswald",sans-serif;font-size:15px;text-align:center;line-height:27px;text-decoration:none}
.arrows{display:flex;gap:8px}

/* side panel */
.side-panel{left:577px;top:429px;width:225px;height:438px;background:var(--panel);border-radius:3px}
.tab-head{left:590px;top:469px;width:199px;height:27px;background:linear-gradient(#4a4a4a,#2a2a2a);color:var(--white);font-family:"Oswald",sans-serif;font-size:12px;line-height:27px;padding-left:11px}
.tab-body{left:590px;top:496px;width:199px;height:299px;background:var(--white);border:1px solid #dcdcdc;border-top:none}
.tab-photo{left:601px;top:509px;width:177px;height:100px;background:linear-gradient(160deg,#6e8a5a 0%,#9a3040 40%,#3d4a7a 70%,#6a9a4a 100%)}
.tab-text{left:601px;top:617px;width:180px;font-size:10.4px;line-height:15.1px;color:var(--muted)}
.read-more{left:716px;top:771px;font-family:"Oswald",sans-serif;font-size:13px;color:var(--red)}
.side-link{left:590px;width:199px;height:30px;background:linear-gradient(#fbfbfb,#ececec);border:1px solid #dcdcdc;font-family:"Oswald",sans-serif;font-size:12px;color:var(--ink);line-height:28px;padding-left:11px}

/* dark band */
.news-band{left:0;top:893px;width:900px;height:224px;background:var(--band)}
.band-heading{font-family:"Oswald",sans-serif;font-weight:400;font-size:17px;color:var(--white);text-transform:uppercase}
.news-thumb{left:97px;width:71px;height:63px;border:2px solid var(--red)}
.news-title{left:182px;font-family:"Oswald",sans-serif;font-weight:400;font-size:15px;color:#e8332e;text-transform:uppercase}
.news-text{left:182px;width:350px;font-size:10.5px;line-height:15px;color:#e6e6e6}
.quote-box{left:577px;top:941px;width:225px;height:121px;background:var(--black)}
.quote-text{left:593px;top:950px;width:205px;font-size:10.4px;line-height:15.2px;color:#e0e0e0;text-indent:30px}
.quote-mark{font-family:"Oswald",sans-serif;font-weight:500;font-size:40px;line-height:1;color:#bdbdbd}
.quote-name{left:577px;top:1080px;font-family:"Oswald",sans-serif;font-size:11px;color:var(--white)}

/* footer */
.site-footer{left:0;top:1117px;width:900px;height:83px;background:var(--red-dark)}
.footer-brand{left:97px;top:1138px;display:flex;align-items:center;gap:7px;font-family:"Oswald",sans-serif;font-weight:500;font-size:12px;line-height:14px;color:var(--white);text-transform:uppercase}
.footer-brand span.mark{width:18px;height:18px;background:var(--white)}
.copyright{left:165px;top:1147px;font-family:"Oswald",sans-serif;font-weight:400;font-size:10.5px;color:var(--white)}
.copyright em{font-style:normal;color:#6e0000}
.footer-nav{right:98px;top:1152px;font-family:"Oswald",sans-serif;font-size:8.5px;color:var(--white);letter-spacing:.2px}
</style>
</head>
<body>

<header class="abs site-header">
  <div class="abs brand" style="left:98px;top:20px">
    <span class="brand-mark"></span>
    <span class="brand-name">Keelstone Rugby<br>Canada</span>
  </div>
  <div class="abs social" aria-label="Social media links">
    <span></span><span></span><span></span><span></span><span></span>
  </div>
  <div class="abs search">
    <svg width="13" height="13" viewBox="0 0 13 13"><circle cx="5" cy="5" r="3.8" fill="none" stroke="#eee" stroke-width="1.6"/><line x1="8" y1="8" x2="12" y2="12" stroke="#eee" stroke-width="2"/></svg>
  </div>
  <nav class="abs main-nav">
    <a class="active" href="#" style="left:423px">HOME</a>
    <a href="#" style="left:477px">PLAYER DEVELOPMENT</a>
    <a href="#" style="left:612px">COMMUNITY</a>
    <a href="#" style="left:698px">KRC NEWS</a>
    <a href="#" style="left:774px">CONTACT US</a>
  </nav>
</header>

<section class="abs hero" role="img" aria-label="Action photo of a rugby player carrying the ball past a tackler"></section>
<p class="abs hero-caption">You are never too old to set another goal or to dream a new dream.</p>
<div class="abs hero-dots"><span></span><span></span><span></span><span></span></div>

<!-- welcome -->
<h1 class="abs heading" style="left:97px;top:429px">Welcome to <em>Keelstone Rugby</em></h1>
<p class="abs body-text" style="left:97px;top:452px;width:470px">Aliquam molestie, mi et imperdiet euismod, dui purus auctor tellus, et interdum lacus lectus et ante. Sed accumsan sollicitudin sapien, sit amet adipiscing turpis gravida ac. In congue, neque ac lobortis volutpat, libero mauris varius mi, vitae suscipit ipsum ligula vitae risus.</p>

<h2 class="abs heading" style="left:97px;top:524px">Our <em>Mission</em></h2>
<div class="abs rule" style="left:97px;top:548px;width:214px"></div>
<p class="abs body-text" style="left:97px;top:558px;width:214px">Keelstone Rugby Canada is about making skilled, informed, and knowledgeable players. Our mission is to develop young players within an environment that is challenging, yet rewarding in order to see them attain their goals in the sport of rugby.</p>

<h2 class="abs heading" style="left:349px;top:524px">Our <em>Vision</em></h2>
<div class="abs rule" style="left:349px;top:548px;width:214px"></div>
<p class="abs body-text" style="left:349px;top:558px;width:216px">We want our players to enjoy their experience and benefit from their efforts. Keelstone Rugby is determined to contribute to rugby in Canada by working with young aspiring<br>players who are willing to sacrifice their time and energy in pursuit of their goals.</p>

<div class="abs hair" style="left:97px;top:684px;width:466px"></div>

<!-- programs -->
<h2 class="abs heading" style="left:97px;top:696px">KRC Club <em>Programs</em></h2>
<div class="abs arrows" style="left:543px;top:697px">
  <svg width="8" height="12" viewBox="0 0 8 12"><path d="M6 1 1 6l5 5" fill="none" stroke="#555" stroke-width="1.6"/></svg>
  <svg width="8" height="12" viewBox="0 0 8 12"><path d="M2 1l5 5-5 5" fill="none" stroke="#555" stroke-width="1.6"/></svg>
</div>
<div class="abs video" role="img" aria-label="Video still of a youth rugby session in an indoor field house">
  <svg class="play" width="34" height="22" viewBox="0 0 34 22"><rect width="34" height="22" rx="5" fill="#222" opacity=".8"/><path d="M13 6l9 5-9 5z" fill="#fff"/></svg>
  <div class="bar"><i></i></div>
</div>
<p class="abs program-title">U10-12</p>
<p class="abs program-lead">Emphasis for this age grade:</p>
<ul class="abs checklist">
  <li><svg width="11" height="9" viewBox="0 0 11 9"><path d="M1 5l3 3 6-7" fill="none" stroke="#d2232a" stroke-width="2"/></svg>Fun &amp; Enjoyment</li>
  <li><svg width="11" height="9" viewBox="0 0 11 9"><path d="M1 5l3 3 6-7" fill="none" stroke="#d2232a" stroke-width="2"/></svg>Skill Introduction</li>
  <li><svg width="11" height="9" viewBox="0 0 11 9"><path d="M1 5l3 3 6-7" fill="none" stroke="#d2232a" stroke-width="2"/></svg>Modified Games</li>
</ul>
<a class="abs btn-register" href="#">REGISTER NOW</a>

<!-- side panel -->
<aside class="abs side-panel"></aside>
<h2 class="abs heading" style="left:589px;top:442px">Player <em>Development</em></h2>
<div class="abs tab-head">THE KRC MODEL</div>
<div class="abs tab-body"></div>
<div class="abs tab-photo" role="img" aria-label="Photo of three young rugby players lying on the grass with a ball"></div>
<p class="abs tab-text">Keelstone Rugby uses a player-centred model of learning that best provides for developmental needs of young aspiring rugby players. Our programs are designed for players ages, 10 to 18, with the understanding that the players need to develop not only the skills but knowledge to best prepare them to accomplish their personal long-term goals in the sport of rugby.</p>
<a class="abs read-more">READ MORE</a>
<div class="abs side-link" style="top:797px">WINTER ACADEMY</div>
<div class="abs side-link" style="top:829px">OUR COACHING STAFF</div>

<!-- news band -->
<section class="abs news-band"></section>
<h2 class="abs band-heading" style="left:97px;top:906px">Latest News from KRC</h2>

<div class="abs news-thumb" style="top:947px;background:linear-gradient(180deg,#9fb08a,#2c2c2c 70%,#4a6a3a)" role="img" aria-label="Photo of a camp group holding certificates"></div>
<h3 class="abs news-title" style="top:943px">Summer Camp Club Tour 2013</h3>
<p class="abs news-text" style="top:965px">This summer, Keelstone Rugby will once again bring the latest skills, drills, and games to Ontario's young and aspiring rugby players. We have a talented staff of current and former junior National team players...</p>
<div class="abs" style="left:94px;top:1023px;width:440px;height:1px;background:#6a6a6a"></div>

<div class="abs news-thumb" style="top:1037px;background:linear-gradient(160deg,#5a7a3a,#3a2a22 50%,#7a5a3a)" role="img" aria-label="Photo of young players in a tackle drill"></div>
<h3 class="abs news-title" style="top:1033px">Summer Camp Club Tour 2013</h3>
<p class="abs news-text" style="top:1055px">This summer, Keelstone Rugby will once again bring the latest skills, drills, and games to Ontario's young and aspiring rugby players. We have a talented staff of current and former junior National team players...</p>

<h2 class="abs band-heading" style="left:577px;top:906px">Testimonials</h2>
<div class="abs arrows" style="left:785px;top:912px">
  <svg width="7" height="11" viewBox="0 0 7 11"><path d="M5.5 1 1.5 5.5l4 4.5" fill="none" stroke="#fff" stroke-width="1.6"/></svg>
  <svg width="7" height="11" viewBox="0 0 7 11"><path d="M1.5 1l4 4.5-4 4.5" fill="none" stroke="#fff" stroke-width="1.6"/></svg>
</div>
<div class="abs quote-box"></div>
<svg class="abs" style="left:636px;top:1061px" width="26" height="16" viewBox="0 0 26 16"><path d="M10 0h16L0 16z" fill="#0c0c0c"/></svg>
<span class="abs quote-mark" style="left:588px;top:944px">“</span>
<p class="abs quote-text">Personally, I see so much benefit to the program you run; there is a definite need for this level of training in our [rugby] community and others. I can't believe the progress that the athletes made and their overall desire to improve for the love of the game.....</p>
<span class="abs quote-mark" style="left:748px;top:1024px">”</span>
<p class="abs quote-name">Dana Colville Assistant Coach</p>

<!-- footer -->
<footer class="abs site-footer"></footer>
<div class="abs footer-brand" style="left:97px;top:1140px"><span class="mark"></span></div>
<p class="abs copyright">Copyright © 2013 <em>Keelstone Rugby Canada.</em> All Right Reserved</p>
<nav class="abs footer-nav">HOME &nbsp;/&nbsp; PLAYER DEVELOPMENT &nbsp;/&nbsp; COMMUNITY &nbsp;/&nbsp; KRC NEWS &nbsp;/&nbsp; CONTACT US</nav>

</body>
</html>
```